Company Values One-Pager

We're a recruitment firm based in Singapore, focused on the startup tech and VC sectors. www.brelvanhire.com

As we're now at the point of growing and hiring, we want a one-pager (PDF or whatever) that summarises us and our company values.

I've attached a short PowerPoint that goes into the values etc.

Font styles to use
Sans Serif

Requirements
Must have
• We like a 'clean' look. Our logo is bright and simple, and that's what we're looking for.
• The official colour code for the logo is seafoam green
• www.huepondlab.com/color/71EEB8/sea_foam_green
• Our website also gives a good insight.
• I'd like logos that summarise each value alongside them. i.e + for positivity, a letter for delivery etc. (Just ideas - please innovate!)
Should not have
• Nothing dark - just keep it simple and fresh

```html
<!DOCTYPE html>
<html lang="en">
<head>
<meta charset="utf-8">
<title>Brelvan Hire – Company Values One-Pager</title>
<link rel="stylesheet" href="https://fonts.googleapis.com/css2?family=Hind:wght@400;500;600;700&family=Questrial&display=swap">
<style>
  :root{
    --seafoam:#3fcf8e;
    --seafoam-light:#71eeb8;
    --ink:#3b3b3b;
    --text:#4a4a4a;
    --muted:#6b6b6b;
    --paper:#f4f4f2;
    --footer-dark:#4b4b4d;
    --backdrop:#8aa3a2;
    --tech-deep:#0b3f86;
    --tech-mid:#1a6fc2;
    --tech-glow:#5fd4f5;
  }
  *{box-sizing:border-box;margin:0;padding:0}
  html,body{width:1200px;height:960px;overflow:hidden}
  body{background:var(--backdrop);font-family:"Questrial",sans-serif;color:var(--text)}
  .flyer{position:absolute;left:282px;top:30px;width:636px;height:900px;background:var(--paper);overflow:hidden;box-shadow:0 6px 18px rgba(0,0,0,.18)}
  .flyer-art{position:absolute;left:0;top:0}
  .header{position:absolute;left:0;top:0;width:636px;height:86px;background:var(--paper);display:flex;align-items:center;justify-content:space-between;padding:0 30px}
  .brand{display:flex;align-items:center;gap:10px}
  .brand-mark{width:18px;height:18px;background:var(--seafoam)}
  .brand-name{font-family:"Hind",sans-serif;font-weight:600;font-size:28px;letter-spacing:3px;color:var(--seafoam);line-height:1}
  .site{display:flex;align-items:center;gap:7px;font-family:"Hind",sans-serif;font-weight:500;font-size:15px;color:#222}
  .site-dot{width:9px;height:9px;border-radius:50%;background:var(--seafoam)}
  .hero-title{position:absolute;left:380px;top:188px;font-family:"Hind",sans-serif;font-weight:600;font-size:40px;color:#bff3ff;letter-spacing:.5px;text-shadow:0 0 10px rgba(95,212,245,.7)}
  .hero-caption{position:absolute;left:518px;top:270px;font-size:13px;color:#8fdcf5}
  .headline{position:absolute;left:30px;top:380px}
  .headline-main{font-family:"Hind",sans-serif;font-weight:700;font-size:26px;color:var(--seafoam);line-height:1.1}
  .headline-sub{font-family:"Hind",sans-serif;font-weight:400;font-size:18px;color:var(--ink);margin-top:2px}
  .column-divider{position:absolute;left:250px;top:466px;width:1px;height:432px;background:#d3d3d3}
  .who{position:absolute;left:30px;top:460px;width:205px}
  .section-title{font-family:"Hind",sans-serif;font-weight:600;font-size:25px;color:var(--ink)}
  .fact{position:absolute;left:0}
  .fact-label{font-family:"Hind",sans-serif;font-weight:700;font-size:13.5px;color:#2e2e2e;line-height:1.2}
  .fact-body{font-size:10.5px;line-height:1.3;color:var(--text);margin-top:2px}
  .values{position:absolute;left:280px;top:466px;width:330px}
  .values-title{font-family:"Hind",sans-serif;font-weight:700;font-size:18px;color:var(--ink)}
  .value{position:absolute;left:0;width:330px}
  .value-head{display:inline-flex;align-items:baseline;gap:8px;border-bottom:1px solid var(--seafoam);padding-bottom:1px}
  .value-name{font-family:"Hind",sans-serif;font-size:15px;color:var(--seafoam);letter-spacing:.4px}
  .value-gloss{font-size:10.5px;color:#2e2e2e}
  .value-desc{font-size:10.5px;line-height:1.3;color:var(--text);margin-top:10px}
  .footer-phone{position:absolute;left:30px;top:848px;font-family:"Hind",sans-serif;font-weight:600;font-size:29px;color:#fff;letter-spacing:.5px}
  .footer-address{position:absolute;left:288px;top:853px;font-size:10.5px;line-height:1.3;color:#e8e8e8}
  .footer-contact{position:absolute;left:468px;top:853px;font-size:10.5px;line-height:1.5;color:#e8e8e8}
  .footer-rule{position:absolute;left:450px;top:846px;width:1px;height:40px;background:#8a8a8a}
</style>
</head>
<body>
<main class="flyer">
  <svg class="flyer-art" width="636" height="900" viewBox="0 0 636 900" aria-hidden="false">
    <defs>
      <radialGradient id="techGlow" cx="0.55" cy="0.4" r="0.75">
        <stop offset="0" stop-color="#3fa9e8"/>
        <stop offset="0.45" stop-color="#1a6fc2"/>
        <stop offset="1" stop-color="#0a2f6b"/>
      </radialGradient>
    </defs>
    <rect role="img" aria-label="Photo of a businessman touching a glowing search icon over a blue digital circuit background" x="0" y="80" width="636" height="420" fill="url(#techGlow)"/>
    <path d="M0 331 C200 298 420 330 636 491 L636 900 L0 900 Z" fill="var(--paper)"/>
    <path d="M370 318 C480 326 570 380 588 486 C556 412 480 352 370 318 Z" fill="#8a8a8a"/>
    <path d="M410 334 C520 344 610 410 636 486 L636 452 C598 396 520 350 410 334 Z" fill="var(--seafoam)"/>
    <rect x="0" y="829" width="636" height="71" fill="var(--footer-dark)"/>
    <polygon points="0,829 246,829 262,900 0,900" fill="var(--seafoam)"/>
    <circle cx="131" cy="829" r="18" fill="var(--paper)"/>
    <circle cx="131" cy="829" r="13" fill="#8c8c8c"/>
    <path d="M124 832 Q124 824 131 824 Q138 824 138 832 Z M127 826 h8 v2 h-8z" fill="#fff"/>
    <path d="M297 847 a4 4 0 1 1 8 0 c0 3 -4 8 -4 8 s-4 -5 -4 -8z" fill="var(--seafoam)"/>
    <circle cx="301" cy="847" r="1.5" fill="var(--footer-dark)"/>
    <rect x="456" y="852" width="9" height="6" fill="var(--seafoam)"/>
    <path d="M456 852 l4.5 3.5 l4.5 -3.5" stroke="var(--footer-dark)" stroke-width="1" fill="none"/>
    <circle cx="460.5" cy="870" r="4" fill="var(--seafoam)"/>
  </svg>

  <header class="header">
    <div class="brand">
      <span class="brand-mark"></span>
      <span class="brand-name">BRELVAN HIRE</span>
    </div>
    <div class="site"><span class="site-dot"></span>www.brelvanhire.com</div>
  </header>

  <div class="hero-title">CORE VALUES</div>
  <div class="hero-caption">search completed</div>

  <section class="headline">
    <h1 class="headline-main">SOUTH-EAST ASIAECOSYSTEM</h1>
    <p class="headline-sub">IN FOR THE STARTUP RECRUITMENT PARTNER</p>
  </section>

  <div class="column-divider"></div>

  <section class="who">
    <h2 class="section-title">WHO WE ARE</h2>
    <div class="fact" style="top:60px">
      <div class="fact-label">WHAT</div>
      <p class="fact-body">We are the 'recruitment partner for the startup ecosystem in South-East Asia'; partnering with Venture Capital and startup tech firms, HQ'd out of Singapore.</p>
    </div>
    <div class="fact" style="top:154px">
      <div class="fact-label">WHO</div>
      <p class="fact-body">Established by Dara Lim &amp; Owen Tasker</p>
    </div>
    <div class="fact" style="top:207px">
      <div class="fact-label">WHEN</div>
      <p class="fact-body">Opened our doors in September 2016</p>
    </div>
    <div class="fact" style="top:262px">
      <div class="fact-label">LONGER-TERM GOAL</div>
      <p class="fact-body">Asia and Global expansion</p>
    </div>
    <div class="fact" style="top:316px">
      <div class="fact-label">CORE VALUES</div>
      <p class="fact-body">Positivity · Proactivity · Teamwork · Delivery</p>
    </div>
  </section>

  <section class="values">
    <h2 class="values-title">OUR CORE VALUES</h2>
    <div class="value" style="top:48px">
      <div class="value-head"><span class="value-name">POSITIVITY</span><span class="value-gloss">the character of being positive</span></div>
      <p class="value-desc">We look on the bright side…<br>and don't let limiting beliefs hold us back</p>
    </div>
    <div class="value" style="top:122px">
      <div class="value-head"><span class="value-name">PROACTIVITY</span><span class="value-gloss">to initiate change rather than reacting to events</span></div>
      <p class="value-desc">We don't wait… we make things happen</p>
    </div>
    <div class="value" style="top:186px">
      <div class="value-head"><span class="value-name">TEAMWORK</span><span class="value-gloss">working together</span></div>
      <p class="value-desc">We work together… to solve problems,<br>find solutions, and celebrate the good times</p>
    </div>
    <div class="value" style="top:266px">
      <div class="value-head"><span class="value-name">DELIVERY</span><span class="value-gloss">to achieve what is desired, expected or promised</span></div>
      <p class="value-desc">We do what we say we're going to do…<br>for our candidates, clients, and colleagues alike</p>
    </div>
  </section>

  <footer>
    <div class="footer-phone">+65 6204 8830</div>
    <div class="footer-address">48 Marlow Road, Tessel House,<br>#05-02, Singapore 068211</div>
    <div class="footer-rule"></div>
    <div class="footer-contact">info@brelvanhire.com<br>www.brelvanhire.com</div>
  </footer>
</main>
</body>
</html>
```